Statement of Capabilities

We are looking for a fresh new stationary (Word Template) and a new look for our statement of capabilities....logo must be the same.

We are an electrical / lighting contractor-

www.BrightwaveUpkeep.com

Target Market(s)

B2B and government agencies

Industry/Entity Type

Electrical

Colors
eb1f27
0655a3

Requirements
Must have
• LOGO

```html
<!DOCTYPE html>
<html lang="en">
<head>
<meta charset="utf-8">
<title>Brightwave Upkeep Letterhead</title>
<link rel="stylesheet" href="https://fonts.googleapis.com/css2?family=Archivo:wght@700;800&family=Questrial&display=swap">
<style>
  :root {
    --brand-red: #eb1f27;
    --brand-blue: #0655a3;
    --ink-grey: #555a60;
    --rule-grey: #c9ccd0;
    --paper: #ffffff;
    --backdrop: #e4e5e7;
  }
  html, body {
    margin: 0;
    padding: 0;
    width: 1200px;
    height: 968px;
    overflow: hidden;
    background: var(--backdrop);
  }
  .letterhead {
    position: absolute;
    left: 262px;
    top: 40px;
    width: 676px;
    height: 888px;
    background: var(--paper);
    box-shadow: 0 2px 10px rgba(0,0,0,0.12);
    overflow: hidden;
  }
  .masthead {
    position: absolute;
    left: 44px;
    top: 40px;
    right: 44px;
    display: flex;
    justify-content: space-between;
    align-items: flex-start;
  }
  .brand {
    display: flex;
    align-items: center;
    gap: 8px;
    flex-shrink: 0;
  }
  .brand-mark {
    width: 13px;
    height: 13px;
    background: var(--brand-red);
  }
  .brand-name {
    font-family: "Archivo", Arial, sans-serif;
    font-weight: 800;
    font-size: 19px;
    line-height: 1.05;
    color: var(--brand-red);
    text-transform: uppercase;
    letter-spacing: 0.2px;
  }
  .services {
    flex-shrink: 0;
    width: 362px;
    margin-top: 34px;
    font-family: "Archivo", Arial, sans-serif;
    font-weight: 700;
    font-size: 6.9px;
    letter-spacing: 0.15px;
    color: var(--brand-blue);
    text-transform: uppercase;
  }
  .services p {
    margin: 0;
    padding: 3px 0 4px;
    border-bottom: 1px solid var(--rule-grey);
    white-space: nowrap;
  }
  .services .sep { color: var(--brand-red); padding: 0 2px; }
  .contact-line {
    position: absolute;
    left: 44px;
    bottom: 44px;
    display: flex;
    align-items: center;
    gap: 22px;
    font-family: "Questrial", Arial, sans-serif;
    font-size: 9px;
    color: var(--ink-grey);
  }
  .contact-item { display: flex; align-items: center; gap: 5px; }
  .contact-icon { width: 10px; height: 10px; display: block; }
  .footer-band {
    position: absolute;
    left: 0;
    right: 0;
    bottom: 0;
    height: 9px;
    background: var(--brand-red);
  }
  .web-tab {
    position: absolute;
    right: 44px;
    bottom: 0;
    height: 24px;
    padding: 0 20px;
    display: flex;
    align-items: center;
    background: var(--brand-blue);
    border-radius: 8px 8px 0 0;
    font-family: "Questrial", Arial, sans-serif;
    font-size: 11px;
    color: #ffffff;
    letter-spacing: 0.2px;
  }
</style>
</head>
<body>
  <main class="letterhead">
    <header class="masthead">
      <div class="brand">
        <span class="brand-mark"></span>
        <span class="brand-name">Brightwave Upkeep<br>Incorporated</span>
      </div>
      <div class="services">
        <p>Roadway<span class="sep">•</span>Security<span class="sep">•</span>Commercial<span class="sep">•</span>Sports Lighting<span class="sep">•</span>Electrical<span class="sep">•</span>Washington DC</p>
        <p>Northern Virginia<span class="sep">•</span>Richmond<span class="sep">•</span>Glenmere<span class="sep">•</span>Gaithersburg</p>
      </div>
    </header>

    <footer>
      <div class="contact-line">
        <span class="contact-address">415 Harbor Ave Suite B, Glenmere Maryland 21077</span>
        <span class="contact-item">
          <svg class="contact-icon" viewBox="0 0 10 10" aria-hidden="true">
            <rect width="10" height="10" rx="2" fill="#eb1f27"/>
            <path d="M3 2.2 L4.2 3.6 L3.6 4.4 Q4.4 5.8 5.6 6.4 L6.4 5.8 L7.8 7 L7.2 7.9 Q4.2 7.8 2.2 2.9 Z" fill="#fff"/>
          </svg>
          877-555-0142
        </span>
        <span class="contact-item">
          <svg class="contact-icon" viewBox="0 0 10 10" aria-hidden="true">
            <rect width="10" height="10" rx="2" fill="#eb1f27"/>
            <rect x="2" y="4" width="6" height="3.6" fill="#fff"/>
            <rect x="3.2" y="2" width="3.6" height="2" fill="#fff"/>
          </svg>
          877-555-0143
        </span>
      </div>
      <div class="footer-band"></div>
      <div class="web-tab">www.BrightwaveUpkeep.com</div>
    </footer>
  </main>
</body>
</html>
```